Flyer for free seminar invite

We are an accident management company.
Need a flyer to invite smash repairers to a free seminar.
Our website is motovista.com.au.
The flyer will be distributed by hand, email and fax.

The seminar will cover:

3 keys to success in 2015

* How to obtain and retain quality fleet work
* How to quote for profit and make insurers pay more
* How to make money from loan vehicles

Please see attached:

* Current brochure
* Logo, artwork

Target Market(s)

car repairers

Industry/Entity Type

Loan

Font styles to use
Sans Serif

Colors
eb1f27

Requirements
Must have
• 1 page
• logo and contact details
• date and location of event
• benefits of attending event
• large font, suitable for faxing

```html
<!DOCTYPE html>
<html lang="en">
<head>
<meta charset="utf-8">
<title>3 Keys to Success in 2015 – Free Seminar</title>
<link rel="stylesheet" href="https://fonts.googleapis.com/css2?family=Tinos:wght@400;700&family=Open+Sans:wght@600;700&family=Arimo:wght@400&display=swap">
<style>
  :root {
    --brand-red: #e31b2b;
    --headline-yellow: #f5ee1c;
    --ink: #111111;
    --paper: #f4f4f4;
    --key-grey-light: #d2d2d2;
    --key-grey-dark: #8a8a8a;
  }
  * { margin: 0; padding: 0; box-sizing: border-box; }
  html, body { width: 1200px; height: 750px; overflow: hidden; background: var(--paper); }
  .flyer {
    position: relative;
    width: 1200px;
    height: 750px;
    background: linear-gradient(180deg, #f8f8f8 0%, #ececec 100%);
    overflow: hidden;
  }
  .key-art {
    position: absolute;
    left: 0; top: 0;
    width: 165px; height: 120px;
    background: linear-gradient(135deg, var(--key-grey-light), var(--key-grey-dark));
    border-bottom-right-radius: 50px;
    opacity: 0.8;
  }
  .headline {
    position: absolute;
    left: 72px; top: 8px;
    font-family: "Tinos", "Times New Roman", serif;
    font-weight: 700;
    line-height: 1;
    white-space: nowrap;
  }
  .headline__number {
    font-size: 158px;
    color: var(--brand-red);
    -webkit-text-stroke: 3px var(--ink);
    text-shadow: 4px 4px 0 var(--ink);
  }
  .headline__word {
    display: inline-block;
    font-size: 150px;
    color: var(--headline-yellow);
    text-shadow: 3px 3px 2px rgba(0,0,0,0.35);
    transform: scaleX(1.18);
    transform-origin: left center;
  }
  .subhead {
    position: absolute;
    font-family: "Tinos", "Times New Roman", serif;
    color: var(--brand-red);
    text-shadow: 1px 2px 2px rgba(0,0,0,0.25);
    line-height: 1;
    white-space: nowrap;
  }
  .subhead--success { left: 98px; top: 150px; font-size: 88px; letter-spacing: 6px; }
  .subhead--year { left: 138px; top: 228px; font-size: 100px; letter-spacing: 5px; }
  .brand {
    position: absolute;
    left: 772px; top: 46px;
    display: flex; align-items: center; gap: 12px;
  }
  .brand__dot { width: 20px; height: 20px; border-radius: 50%; background: var(--brand-red); }
  .brand__name {
    font-family: "Tinos", "Times New Roman", serif;
    font-size: 52px;
    color: var(--ink);
  }
  .contact {
    position: absolute;
    left: 776px; top: 150px;
    font-family: "Arimo", Arial, sans-serif;
    color: var(--brand-red);
  }
  .contact__web { font-size: 22px; margin-left: 26px; margin-bottom: 12px; }
  .contact__list { display: grid; grid-template-columns: 102px auto; row-gap: 2px; font-size: 19px; }
  .topics {
    position: absolute;
    left: 0; right: 0; top: 340px;
    list-style: none;
    text-align: center;
    font-family: "Open Sans", Arial, sans-serif;
    font-weight: 600;
    font-size: 45px;
    line-height: 58px;
    color: var(--brand-red);
  }
  .event {
    position: absolute;
    left: 28px; top: 560px;
    width: 262px;
    font-family: "Open Sans", Arial, sans-serif;
    font-weight: 600;
    color: var(--ink);
    font-size: 19px;
    line-height: 27px;
  }
  .event__title {
    display: inline-block;
    background: var(--brand-red);
    color: #ffffff;
    font-weight: 700;
    font-size: 26px;
    line-height: 1;
    padding: 8px 12px;
    margin-bottom: 10px;
  }
  .event__venue { color: var(--brand-red); }
  .repair-art {
    position: absolute;
    left: 320px; top: 560px;
    width: 880px; height: 190px;
    background: linear-gradient(180deg, rgba(227,27,43,0.55) 0%, var(--brand-red) 100%);
    border-top-left-radius: 300px 110px;
    border-top-right-radius: 120px 80px;
  }
</style>
</head>
<body>
  <main class="flyer">
    <div class="key-art" role="img" aria-label="Silver car key illustration"></div>

    <h1 class="headline"><span class="headline__number">3</span><span class="headline__word">keys</span></h1>
    <p class="subhead subhead--success">to success</p>
    <p class="subhead subhead--year">in 2015</p>

    <div class="brand">
      <span class="brand__dot"></span>
      <span class="brand__name">MOTOVISTA</span>
    </div>

    <div class="contact">
      <p class="contact__web">www.motovista.com.au</p>
      <div class="contact__list">
        <span>Phone :</span><span>(02) 9000 1234</span>
        <span>Fax :</span><span>(02) 9000 5678</span>
        <span>Email :</span><span>contact@motovista.com.au</span>
      </div>
    </div>

    <ul class="topics">
      <li>How to obtain and retain quality fleet work</li>
      <li>How to quote for profit and make insurers pay more</li>
      <li>How to make money from loan vehicles</li>
    </ul>

    <section class="event">
      <p class="event__title">FREE SEMINAR</p>
      <p>Thursday 12 March 2015</p>
      <p>6:30pm – 9:00pm</p>
      <p class="event__venue">Riverside Function Centre</p>
    </section>

    <div class="repair-art" role="img" aria-label="Red silhouette of a car with its bonnet open and a mechanic holding a spanner"></div>
  </main>
</body>
</html>
```